Design a two sided Flyer for Each Porch direct mailing from NTPK - size 8,5" x 11"

We need a flyer that will be accepted by NTPK for each porch direct mailing (size 8,5" x 11"). It needs to be double sided designed and we have already made the copy writing. We just need a designer to make it look stunning and chique. When our potential customers receive the flyer they should have a feeling that they can improve their house with the right kind of modern lighting. The flyer should be saying in the front cozy, safety, warmth, in short everything you need at home for the winter. (and they can off course buy that at our web store). Having (happy) people on the flyer a bonus. And in the back it will give a couple tips and tricks on how you should light up your home.

We have included in attachment
- a word document with the writing that needs to go on the flyer (front and back)
- our logo in several files and formats

Under are links to our fileharbor where you can find many pictures of the lamps we sell but feel free to find others.
- https://www.fileharbor.example/sh/qk4tn7z2ab8wyr/p9LmQrTvHs
- https://www.fileharbor.example/sh/81bvc5d6qw0pe3n/hKT2xJ7nVa
- https://www.fileharbor.example/sh/tyw3s8kpl46vqnr/_27xYz9Q4R
- https://www.fileharbor.example/sh/fed31u75840mcsr/_pwHNbqrt8

Last but not least our own site:
- http://www.brevanto.example

Target Market(s)

USA Families in the age of 25-45y old. Medium to high income and open minded

Industry/Entity Type

House

Requirements
Must have
• - minimum of 350 dpi (dot per inch) resolution.
- size 8.5" x 11"
- two sided
- should grab the attention of the reader and give a sense of class, cozy and warmth
Should not have
• no cheap looking, screaming words, flyer

```html
<!DOCTYPE html>
<html lang="en">
<head>
<meta charset="utf-8">
<title>Brevanto – Interior Lighting Flyer</title>
<link href="https://fonts.googleapis.com/css2?family=Open+Sans:wght@400;600;700;800&family=Source+Sans+3:wght@400;600;700&family=Cabin:wght@400;500;600&display=swap" rel="stylesheet">
<style>
  :root {
    --orange: #ee8a24;
    --orange-soft: #f6c08a;
    --brown: #7a4438;
    --brown-dark: #5e3128;
    --cream: #f3e2b3;
    --ink: #2a2a2a;
    --paper: #ffffff;
    --mist: #eeeeee;
  }
  * { box-sizing: border-box; margin: 0; padding: 0; }
  html, body { width: 1200px; height: 840px; overflow: hidden; background: var(--paper); }
  .canvas { position: relative; width: 1200px; height: 840px; background: var(--paper); }

  .flyer { position: absolute; top: 50px; width: 562px; height: 720px; overflow: hidden; }
  .flyer-front { left: 26px; }
  .flyer-back { left: 612px; width: 560px; background: linear-gradient(180deg, #f4f4f4 0%, #ececec 100%); }

  .flyer-art { position: absolute; inset: 0; width: 100%; height: 100%; }

  /* Front */
  .brand { position: absolute; left: 22px; top: 34px; display: flex; align-items: center; gap: 10px; }
  .brand-name { font-family: "Open Sans", sans-serif; font-weight: 400; font-size: 46px; color: var(--orange); letter-spacing: 0.5px; line-height: 1; }
  .brand-dot { width: 22px; height: 22px; border-radius: 50%; background: var(--orange); }

  .front-headline { position: absolute; left: 20px; top: 618px; font-family: "Open Sans", sans-serif; font-weight: 700; font-size: 31px; color: #fff; letter-spacing: 0.2px; }
  .front-intro { position: absolute; left: 20px; top: 660px; width: 470px; font-family: "Open Sans", sans-serif; font-weight: 600; font-size: 10.5px; line-height: 1.45; color: #fff; }
  .front-url { position: absolute; right: 18px; top: 694px; font-family: "Open Sans", sans-serif; font-weight: 700; font-size: 14px; color: #fff; }

  /* Back */
  .guide { position: absolute; left: 22px; right: 22px; top: 70px; font-family: "Source Sans 3", sans-serif; font-size: 10.2px; line-height: 1.45; color: var(--ink); }
  .guide-title { font-family: "Cabin", sans-serif; font-weight: 500; font-size: 19px; color: var(--orange); text-align: center; margin-bottom: 6px; }
  .guide-intro { text-align: center; font-size: 11px; padding: 0 10px; margin-bottom: 10px; }
  .tip h3 { font-family: "Source Sans 3", sans-serif; font-weight: 700; font-size: 11.5px; color: var(--orange); margin-top: 3px; }
  .tip p { margin: 0; }
  .tip-right { text-align: right; }

  .calc-title { font-family: "Open Sans", sans-serif; font-weight: 600; font-size: 14px; color: #111; margin: 12px 0 8px; }
  .calc { width: 100%; border-collapse: collapse; background: #fff; font-family: "Source Sans 3", sans-serif; font-size: 8.6px; color: #333; }
  .calc td { border: 1px solid #8a8a8a; padding: 2px 4px; vertical-align: top; }
  .calc .tall td { height: 38px; }
  .calc .size td { height: 22px; }
  .calc .num { text-align: left; width: 40px; }
  .calc .note { text-align: center; font-size: 9.2px; }
</style>
</head>
<body>
<main class="canvas">

  <!-- Front side -->
  <section class="flyer flyer-front" aria-label="Flyer front">
    <svg class="flyer-art" viewBox="0 0 562 720" preserveAspectRatio="none" aria-hidden="true">
      <defs>
        <linearGradient id="roomTone" x1="0" y1="0" x2="0" y2="1">
          <stop offset="0" stop-color="#e9d9c2"/>
          <stop offset="0.3" stop-color="#b89272"/>
          <stop offset="0.55" stop-color="#6b4a36"/>
          <stop offset="0.75" stop-color="#7b8a5c"/>
          <stop offset="1" stop-color="#3a2518"/>
        </linearGradient>
      </defs>
      <rect width="562" height="720" fill="#ffffff"/>
      <path d="M0 150 C 170 120 360 50 562 22 V 0 H 562 V 75 C 380 95 190 150 0 205 Z" fill="var(--brown)"/>
      <path d="M0 205 C 190 150 380 95 562 75 V 610 H 0 Z" fill="url(#roomTone)" role="img" aria-label="Photo of a dining room lit by a patterned pendant lamp, with large windows onto a garden"/>
      <path d="M0 590 C 160 560 330 630 562 560 V 720 H 0 Z" fill="var(--cream)"/>
      <path d="M0 606 C 170 576 340 646 562 578 V 720 H 0 Z" fill="var(--brown)"/>
    </svg>
    <div class="brand"><span class="brand-name">brevanto</span><span class="brand-dot"></span></div>
    <h1 class="front-headline">YOUR STYLE. YOUR LIGHTS.</h1>
    <p class="front-intro">Your style, your lights! Brevanto offers a hand-picked contemporary European style selection in decorative lighting and lamps that fits your life.</p>
    <p class="front-url">http://www.brevanto.example</p>
  </section>

  <!-- Back side -->
  <section class="flyer flyer-back" aria-label="Flyer back">
    <svg class="flyer-art" viewBox="0 0 560 720" preserveAspectRatio="none" aria-hidden="true">
      <path d="M0 20 C 180 34 380 30 560 18 V 30 C 380 42 180 46 0 34 Z" fill="var(--orange)"/>
      <path d="M0 36 C 180 48 380 44 560 34 V 38 C 380 48 180 52 0 40 Z" fill="var(--orange-soft)"/>
      <path d="M0 692 C 180 676 380 680 560 694 V 700 C 380 688 180 684 0 700 Z" fill="var(--orange-soft)"/>
      <path d="M0 702 C 180 688 380 690 560 704 V 714 C 380 700 180 698 0 714 Z" fill="var(--orange)"/>
    </svg>

    <article class="guide">
      <h2 class="guide-title">Your guide to the perfect interior lighting</h2>
      <p class="guide-intro">The best light there is, is natural light. However with the winter in-sight and daytime light shrinking, we more and more depend on artificial lights and to light up our living spaces and make our homes sparkle in the dark, feel warmer, cozier and safer. If you contemplating new light fixtures for your house, here are few hints to help you choose the right luminaire.</p>

      <div class="tip">
        <h3>Determine what your lighting goals are.</h3>
        <p>Direct or task lighting is focused in the space you are trying to work. Ambient or indirect lighting is used for ambiance and for overall lighting of a space. Once chosen you can begin to choose lighting options. Each room in your home should have a mood you want to set, as well as a function you want your lighting to serve. Choose the right amount of light for your room by using the calculation under.</p>
      </div>

      <div class="tip tip-right">
        <h3>Use multiple light sources for one space.</h3>
        <p>This will help you to achieve a variety of functions and activities in one space and it will reduce shadows. Have a mix of light sources at different levels (recessed, suspension lamps, wall scones,…) to create a flattering ambience and add appropriate task lighting for whatever you do in that space. In the kitchen, under counter lights can provide great task lighting. While in a living room, opt for a floor lamp next to a couch or favorite reading chair</p>
      </div>

      <div class="tip">
        <h3>Choose your chandeliers wisely.</h3>
        <p>Because of the central position in a space a chandelier determines largely the decorating value of it. Ask yourself if you want it to be an eye catcher or should it blend in? In any way and whichever is your décor choice, measure out the space, and ceiling height before ordering to ensure enough head room will be available below the hanging chandelier.</p>
      </div>

      <div class="tip tip-right">
        <h3>Highlight the room's highlights.</h3>
        <p>Dramatize wall textures, accent artwork or light up the fireplace. Draw the attention within the space to the architecture and decorative highlights of it. You can do this with special adjustable spot lighting that is either recessed or on a track or use upwards lighting wall scones.</p>
      </div>

      <div class="tip">
        <h3>Go for green and save!</h3>
        <p>85% of the cost of lighting are energy costs so it pays off rather fast to switch to energy saving alternatives like LED. A little bit more expensive at the registry but far cheaper on your next energy bill. Don't like the white color? Look on the packaging for the color temperature; 2700K is perfect for ambiance, 3000K for task lighting.</p>
      </div>

      <h2 class="calc-title">Calculate yourself how much light you really need</h2>
      <table class="calc">
        <tr class="size">
          <td>How big is the area?</td>
          <td>Width &nbsp;(A)</td>
          <td></td>
          <td>Length (B)</td>
          <td colspan="2">Surface (A)x(B)</td>
          <td style="text-align:right">(C)</td>
        </tr>
        <tr class="tall">
          <td>What is the purpose of the area?</td>
          <td colspan="2">LED or CFLI lighting</td>
          <td>Total Lumen needed<br>(C) x (D)</td>
          <td colspan="2">Incandescent lighting</td>
          <td>Total Watt needed<br>(C) x (E)</td>
        </tr>
        <tr>
          <td>Relax, Watch TV, Talk</td>
          <td>Lumen per Sq ft (D)</td><td class="num">20</td>
          <td></td>
          <td>Watt per Sq ft (E)</td><td class="num">1.5</td>
          <td></td>
        </tr>
        <tr>
          <td>Have dinner, dress up</td>
          <td>Lumen per Sq ft (D)</td><td class="num">30</td>
          <td></td>
          <td>Watt per Sq ft (E)</td><td class="num">2</td>
          <td></td>
        </tr>
        <tr>
          <td>Cook, Work, Read,</td>
          <td>Lumen per Sq ft (D)</td><td class="num">50</td>
          <td></td>
          <td>Watt per Sq ft (E)</td><td class="num">3.5</td>
          <td></td>
        </tr>
        <tr>
          <td class="note" colspan="7">Simple add up the wattage or Lumen of the light bulbs in the space to see if you meet the total light needed</td>
        </tr>
      </table>
    </article>
  </section>

</main>
</body>
</html>
```